Building company business card

Design and print business cards for BREVOTA PTY LTD.
A residantial homes building company.
Pixel Forge already designed the company Logo.

```html
<!DOCTYPE html>
<html lang="en">
<head>
<meta charset="utf-8">
<title>BREVOTA PTY LTD – Business Card</title>
<link href="https://fonts.googleapis.com/css2?family=Josefin+Sans:wght@400;600;700&display=swap" rel="stylesheet">
<style>
  :root {
    --navy: #23286a;
    --navy-deep: #161a52;
    --white: #ffffff;
    --paper: #f1f1f3;
    --gold: #d9a437;
    --gold-light: #f0c35a;
    --gold-dark: #a8761c;
    --stage: #e7e4df;
    --font: "Josefin Sans", sans-serif;
  }
  * { margin: 0; padding: 0; box-sizing: border-box; }
  html, body { width: 1200px; height: 900px; overflow: hidden; }
  body {
    background: var(--stage);
    font-family: var(--font);
    position: relative;
  }
  .card {
    position: absolute;
    left: 250px;
    width: 700px;
    height: 400px;
    overflow: hidden;
    box-shadow: 0 10px 24px rgba(0,0,0,0.18);
  }
  .card--back { top: 35px; }
  .card--front { top: 465px; }

  .back-pattern {
    position: absolute; inset: 0;
    background: var(--navy);
  }

  .front-shapes { position: absolute; inset: 0; width: 100%; height: 100%; }

  .holder { position: absolute; left: 52px; top: 58px; }
  .holder__name {
    color: var(--gold);
    font-size: 22px;
    font-weight: 400;
    letter-spacing: 0.5px;
  }
  .holder__role {
    color: var(--white);
    font-size: 19px;
    font-weight: 400;
    margin-top: 4px;
  }

  .contacts {
    position: absolute; left: 70px; top: 168px;
    color: var(--white);
    font-size: 18px;
    list-style: none;
  }
  .contacts li { display: flex; align-items: center; gap: 8px; height: 27px; }
  .contacts .gap { height: 14px; }
  .contacts svg { width: 14px; height: 16px; flex: none; }

  .divider {
    position: absolute; left: 60px; top: 300px;
    width: 270px; height: 1px;
    background: var(--gold);
  }
  .address {
    position: absolute; left: 72px; top: 318px;
    color: var(--white);
    font-size: 18px;
  }

  .company-name {
    position: absolute; left: 486px; top: 100px;
    color: var(--navy);
    font-size: 42px;
    font-weight: 700;
    letter-spacing: 0.5px;
    white-space: nowrap;
  }

  .registration {
    position: absolute; left: 420px; top: 292px;
    color: var(--navy-deep);
    font-size: 14px;
    transform: rotate(-12deg);
    transform-origin: left center;
    white-space: nowrap;
  }
</style>
</head>
<body>

  <section class="card card--back" aria-label="Card back">
    <div class="back-pattern" role="img" aria-label="Navy background with a faint repeating pattern of the company symbol and a small gold symbol"></div>
  </section>

  <section class="card card--front" aria-label="Card front">
    <svg class="front-shapes" viewBox="0 0 700 400" preserveAspectRatio="none" aria-hidden="true">
      <defs>
        <linearGradient id="goldBand" x1="0" y1="1" x2="1" y2="0">
          <stop offset="0" stop-color="var(--gold-dark)"/>
          <stop offset="0.55" stop-color="var(--gold)"/>
          <stop offset="1" stop-color="var(--gold-light)"/>
        </linearGradient>
        <linearGradient id="whiteField" x1="0" y1="0" x2="1" y2="0">
          <stop offset="0" stop-color="var(--paper)"/>
          <stop offset="1" stop-color="var(--white)"/>
        </linearGradient>
      </defs>
      <rect class="field-navy" width="700" height="400" fill="var(--navy)"/>
      <polygon class="strip-deep" points="312,0 348,0 540,232 500,246" fill="var(--navy-deep)"/>
      <polygon class="field-white" points="348,0 700,0 700,198 570,212 540,232" fill="url(#whiteField)"/>
      <polygon class="band-gold" points="55,400 570,210 700,196 700,400" fill="url(#goldBand)"/>
      <polyline class="band-edge" points="55,400 570,210 700,196" fill="none" stroke="var(--gold-dark)" stroke-width="2"/>
    </svg>

    <div class="holder">
      <p class="holder__name">ANDREAS (Andy) KOSTAS</p>
      <p class="holder__role">Director</p>
    </div>

    <ul class="contacts">
      <li>
        <svg viewBox="0 0 14 16"><rect x="3" y="1" width="8" height="14" rx="1.5" fill="none" stroke="var(--gold)" stroke-width="1.3"/></svg>
        0412 550 318
      </li>
      <li>
        <svg viewBox="0 0 14 16"><rect x="3" y="1" width="8" height="14" rx="1.5" fill="none" stroke="var(--gold)" stroke-width="1.3"/></svg>
        0438 206 741
      </li>
      <li class="gap"></li>
      <li>
        <svg viewBox="0 0 14 16"><path d="M1 6 Q7 1 13 6 L11 8 L9 6.5 L5 6.5 L3 8 Z M3 9 H11 V14 H3 Z" fill="var(--gold)"/></svg>
        0412 550 318
      </li>
      <li>
        <svg viewBox="0 0 14 16"><rect x="1" y="4" width="12" height="9" fill="var(--gold)"/><path d="M1 4 L7 9 L13 4" fill="none" stroke="var(--navy)" stroke-width="1.2"/></svg>
        akc@brevota-pl.com
      </li>
    </ul>

    <div class="divider"></div>
    <p class="address">PO Box 482, Kelvale East Vic 3199</p>

    <p class="company-name">BREVOTA</p>

    <p class="registration">ABN - 21 408 552 617 | CDB- U 40918</p>
  </section>

</body>
</html>
```